Create Lanternfield HR Business Cards.

Create Business Cards for Lanternfield HR. 2 sided and Would like the back to have the logo.

Info for Business Card:
Address: 4827 Millbrook Ave Suite 230 Cleveland, Ohio 44987
Office Number: 216-555-0143
Mobile: 216-555-0192

Website: www.lanternfieldhr.example

Target Market(s)

Small to medium size businesses

Industry/Entity Type

Human Resources

Contact Information for Business Card

Company logo and information

Font styles to use
Serif
Sans Serif

Requirements
Must have
• Info for Business Card: Address: 4827 Millbrook Ave Suite 230 Cleveland, Ohio 44987 Office Number: 216-555-0143 Mobile: 216-555-0192 Website: www.lanternfieldhr.example

```html
<!DOCTYPE html>
<html lang="en">
<head>
<meta charset="utf-8">
<title>Lanternfield HR Business Cards</title>
<link href="https://fonts.googleapis.com/css2?family=Arimo:wght@400;700&display=swap" rel="stylesheet">
<style>
  :root {
    --backdrop: #3f3f3f;
    --card-white: #ffffff;
    --brand-orange: #ff8505;
    --brand-navy: #262261;
    --text-grey: #4a4a4a;
    --muted-grey: #7a7a7a;
  }
  * { box-sizing: border-box; margin: 0; padding: 0; }
  html, body {
    width: 1200px; height: 803px; overflow: hidden;
    background: var(--backdrop);
    font-family: "Arimo", Arial, sans-serif;
  }
  .stage {
    position: relative; width: 1200px; height: 803px;
    display: flex; align-items: center; justify-content: center; gap: 60px;
  }
  .card {
    position: relative; width: 520px; height: 297px;
    border-radius: 18px; overflow: hidden;
  }
  /* Front */
  .card-front { background: var(--card-white); }
  .contact {
    position: absolute; top: 34px; right: 34px; text-align: right;
    color: var(--text-grey); font-size: 12.5px; line-height: 1.35;
  }
  .contact-name {
    color: var(--brand-navy); font-weight: 700; font-size: 22px;
    letter-spacing: 0.3px; line-height: 1.05;
  }
  .contact-title { color: var(--muted-grey); font-size: 12px; margin-bottom: 14px; }
  .contact-address { margin-bottom: 14px; }
  .phone-line { display: flex; justify-content: flex-end; align-items: center; gap: 6px; }
  .phone-line svg { width: 11px; height: 11px; flex: none; }
  .web-band {
    position: absolute; right: 0; bottom: 0; width: 282px; height: 30px;
    background: var(--brand-orange); border-top-left-radius: 15px;
    color: var(--card-white); font-size: 13px;
    display: flex; align-items: center; justify-content: flex-end; padding-right: 34px;
  }
  .brand-mark {
    position: absolute; left: 34px; bottom: 40px;
    display: flex; align-items: center; gap: 10px;
  }
  .brand-dot { width: 22px; height: 22px; border-radius: 50%; background: var(--brand-orange); }
  .brand-name { font-weight: 700; font-size: 28px; color: var(--brand-navy); }
  /* Back */
  .card-back {
    background: var(--brand-orange);
    display: flex; align-items: center; justify-content: center;
  }
  .card-back .brand-name { color: var(--card-white); font-size: 44px; }
  .card-back .brand-dot { width: 36px; height: 36px; background: var(--card-white); }
  .card-back .brand-mark { position: static; gap: 14px; }
</style>
</head>
<body>
<main class="stage">
  <section class="card card-front" aria-label="Business card front">
    <div class="contact">
      <div class="contact-name">DANIEL REYES</div>
      <div class="contact-title">President</div>
      <div class="contact-address">4827 Millbrook Ave<br>Suite 230<br>Cleveland, Ohio 44987</div>
      <div class="phone-line">216-555-0143
        <svg viewBox="0 0 12 12" aria-label="Office"><path d="M3 1 L5 3.5 L4 5 Q5.5 7 7 8 L8.5 7 L11 9 L9.5 11 Q4 10 1 2.5 Z" fill="var(--brand-orange)"/></svg>
      </div>
      <div class="phone-line">216-555-0192
        <svg viewBox="0 0 12 12" aria-label="Mobile"><rect x="3" y="0.8" width="6" height="10.4" rx="1" fill="none" stroke="var(--brand-orange)" stroke-width="1.4"/></svg>
      </div>
    </div>
    <div class="brand-mark">
      <span class="brand-dot"></span>
      <span class="brand-name">Lanternfield HR</span>
    </div>
    <div class="web-band">www.lanternfieldhr.example</div>
  </section>

  <section class="card card-back" aria-label="Business card back">
    <div class="brand-mark">
      <span class="brand-dot"></span>
      <span class="brand-name">Lanternfield HR</span>
    </div>
  </section>
</main>
</body>
</html>
```